Plumwick Inc. Website & Vexpad Apps Landing Pages

We need a web site design for our company. We develop software and do various consultant projects for our clients. Our products focus on the mobile platform, mainly the Vexpad (business, games, social, etc.). We want to communicate that our software is simple and good as candy. The web pages should be fun to look at not loosing seriousness and credibility. Web 2.0 style and 960 grid system a must. We are opened to any overall site colour scheme suggestions (look at the sites we like below).

Must haves:
- Our logo should be seen on the site and look great on it :-) (preview attached below)
- Main home page and app landing page.
- Section links/tabs on the home page (home,apps,support,blog,contact,about)
- No text in images
- Style sheet

Looks we like:
- http://k7r2mqx9tvbnwa.stashgrove.net/412_Zunder_Site/final_large.jpg
- http://k7r2mqx9tvbnwa.stashgrove.net/Select_81_Painterly_Vexpad_Landing_Page/final.jpg
- http://gruvlets.com/
- http://mondrake.ca/
- http://lumfold.com/

Industry/Entity Type

Business

Requirements
Must have
• - Company logo should look great on pages.
• - Main home page and app landing page.
• - Section links/tabs on the home page (home,apps,support,blog,contact,about)
• - Web 2.0 style.
• - 960 grid system (12 col, 16 col).
• - Sliced ann optmized
• - Exported in all major formats (psd,ai,eps,png,jpeg,etc)
• - Style sheet
Should not have
• - Text in images

```html
<!DOCTYPE html>
<html lang="en">
<head>
<meta charset="utf-8">
<title>Plumwick — We Sweeten Software &amp; Apps</title>
<link rel="stylesheet" href="https://fonts.googleapis.com/css2?family=Lobster&family=Montserrat:wght@700;800&family=Open+Sans:wght@400;600;700&family=Lora:ital@1&display=swap">
<style>
  :root {
    --bar: #232323;
    --candy-red: #d8141f;
    --candy-red-dark: #a90d15;
    --ink: #1f1712;
    --body-text: #4e4e4e;
    --sky-top: #ffffff;
    --sky-mid: #dde9fb;
    --sky-bottom: #c8dbf8;
    --sky-band: #a7c7f6;
    --page: #efefef;
    --rule: #bdbdbd;
    --ribbon-top: #bcd3f3;
    --ribbon-bottom: #8caee0;
    --white: #ffffff;
  }
  * { box-sizing: border-box; margin: 0; padding: 0; }
  html, body { width: 1200px; height: 900px; overflow: hidden; }
  body { position: relative; font-family: "Open Sans", Arial, sans-serif; background: var(--page); color: var(--body-text); }
  a { color: inherit; text-decoration: none; }
  .abs { position: absolute; }

  /* Header */
  .site-header { left: 0; top: 0; width: 1200px; height: 84px; background: var(--bar); }
  .brand { left: 132px; top: 24px; display: flex; align-items: center; gap: 10px; color: var(--white); font-size: 30px; font-weight: 600; letter-spacing: -0.5px; }
  .brand-dot { width: 22px; height: 22px; border-radius: 50%; background: var(--candy-red); }
  .phone-line { left: 928px; top: 10px; color: var(--white); font-size: 14px; font-weight: 700; letter-spacing: 0.5px; }
  .main-nav { top: 48px; color: var(--white); font-size: 15px; font-weight: 600; }
  .main-nav.current::before, .main-nav.current::after { color: var(--candy-red); font-size: 20px; font-weight: 400; position: absolute; top: -4px; }
  .main-nav.current::before { content: "{"; left: -12px; }
  .main-nav.current::after { content: "}"; right: -12px; }

  /* Hero */
  .hero { left: 0; top: 84px; width: 1200px; height: 366px; background: linear-gradient(180deg, var(--sky-top) 0%, var(--sky-mid) 50%, var(--sky-bottom) 100%); }
  .hero-band { left: 0; top: 450px; width: 1200px; height: 42px; background: var(--sky-band); border-top: 1px solid #eaf2ff; }
  .lower { left: 0; top: 492px; width: 1200px; height: 346px; background: linear-gradient(180deg, #e9e9e9 0%, #f7f7f7 30%, #ffffff 100%); }

  .headline { left: 138px; top: 174px; font-family: "Montserrat", Arial, sans-serif; font-weight: 800; font-size: 44px; line-height: 44px; color: var(--ink); letter-spacing: -1.5px; }
  .strike { left: 262px; top: 180px; }
  .sweeten { left: 306px; top: 118px; font-family: "Lobster", cursive; font-size: 44px; color: var(--candy-red); transform: rotate(-4deg);
    text-shadow: 2px 0 0 #fff, -2px 0 0 #fff, 0 2px 0 #fff, 0 -2px 0 #fff, 2px 2px 0 #fff, -2px -2px 0 #fff, 2px -2px 0 #fff, -2px 2px 0 #fff, 0 4px 5px rgba(0,0,0,.25); }
  .hero-copy { left: 142px; top: 282px; font-size: 14px; line-height: 24px; color: var(--body-text); }
  .cta { left: 139px; top: 377px; width: 165px; height: 41px; border-radius: 8px; background: linear-gradient(180deg, #e52b35, var(--candy-red-dark)); box-shadow: 0 2px 3px rgba(0,0,0,.25); color: var(--white); font-family: "Montserrat", Arial, sans-serif; font-weight: 700; font-size: 16px; display: flex; align-items: center; justify-content: center; letter-spacing: .3px; }

  .device-photo { left: 712px; top: 133px; width: 212px; height: 415px; border-radius: 30px; background: linear-gradient(180deg, #2a2a2a 0%, #b8323a 45%, #d8434a 60%, #2a2a2a 100%); }
  .candy-photo { left: 635px; top: 470px; width: 80px; height: 80px; border-radius: 50%; background: linear-gradient(135deg, #f3c9c8, #d8141f); }
  .tagline { left: 612px; top: 238px; font-family: "Lobster", cursive; font-size: 62px; color: var(--white); transform: rotate(-9deg); white-space: nowrap;
    text-shadow: 4px 0 0 var(--candy-red), -4px 0 0 var(--candy-red), 0 4px 0 var(--candy-red), 0 -4px 0 var(--candy-red), 3px 3px 0 var(--candy-red), -3px -3px 0 var(--candy-red), 3px -3px 0 var(--candy-red), -3px 3px 0 var(--candy-red), 0 10px 10px rgba(0,0,0,.35); }

  /* Content */
  .section-label { font-family: "Lobster", cursive; color: var(--candy-red); font-size: 24px; white-space: nowrap;
    text-shadow: 2px 0 0 #fff, -2px 0 0 #fff, 0 2px 0 #fff, 0 -2px 0 #fff, 2px 2px 0 #fff, -2px -2px 0 #fff, 2px -2px 0 #fff, -2px 2px 0 #fff, 0 2px 4px rgba(0,0,0,.3); transform: rotate(-2deg); }
  .app-icon { left: 141px; top: 562px; width: 132px; height: 120px; border-radius: 10px; background: linear-gradient(90deg, #4a4e62 0%, #e4e6ec 35%, #e4e6ec 70%, #4a4e62 100%); }
  .item-title { color: var(--candy-red); font-size: 19px; font-weight: 400; }
  .item-text { font-size: 14px; line-height: 24px; color: var(--body-text); }
  .more-link { color: var(--candy-red); font-size: 14px; font-weight: 600; }
  .testimonial { left: 690px; top: 586px; font-family: "Lora", Georgia, serif; font-style: italic; font-size: 16.5px; line-height: 30px; color: #555; }
  .testimonial-author { left: 935px; top: 684px; color: var(--candy-red); font-size: 15px; }
  .divider { left: 128px; top: 721px; width: 960px; height: 1px; background: var(--rule); }
  .post-date { left: 299px; top: 732px; font-size: 13px; font-weight: 700; color: #444; letter-spacing: .3px; }
  .social-ribbon { left: 659px; top: 721px; }
  .social-name { left: 659px; top: 738px; width: 117px; text-align: center; color: var(--white); font-size: 17px; font-weight: 700; }
  .social-follow { left: 659px; top: 785px; width: 120px; text-align: center; color: #777; font-size: 14px; }
  .update { left: 799px; top: 739px; font-size: 14px; line-height: 24px; color: var(--body-text); }

  /* Footer */
  .site-footer { left: 0; top: 838px; width: 1200px; height: 62px; background: var(--bar); }
  .footer-nav { top: 856px; color: var(--white); font-size: 14px; }
</style>
</head>
<body>

<header class="abs site-header"></header>
<a class="abs brand" href="#"><span class="brand-dot"></span>Plumwick</a>
<div class="abs phone-line">1 {800} 555-0142</div>
<nav>
  <a class="abs main-nav current" style="left:624px" href="#">home</a>
  <a class="abs main-nav" style="left:692px" href="#">apps</a>
  <a class="abs main-nav" style="left:754px" href="#">support</a>
  <a class="abs main-nav" style="left:837px" href="#">blog</a>
  <a class="abs main-nav" style="left:896px" href="#">contact</a>
  <a class="abs main-nav" style="left:978px" href="#">about</a>
</nav>

<section class="abs hero"></section>
<div class="abs hero-band"></div>
<div class="abs lower"></div>

<h1 class="abs headline">WE DEVELOP<br>SOFTWARE&amp; APPS</h1>
<svg class="abs strike" width="210" height="50" viewBox="0 0 210 50" aria-hidden="true">
  <path d="M4 26 C60 14 120 14 206 44" stroke="#d8141f" stroke-width="6" fill="none" stroke-linecap="round"/>
</svg>
<div class="abs sweeten">Sweeten</div>
<p class="abs hero-copy">Our products focus on the mobile platform.<br>Whatever your project {business, games, social, etc.}<br>we will make your app as sweet as candy.</p>
<a class="abs cta" href="#">LEARN MORE</a>

<div class="abs device-photo" role="img" aria-label="Photo of a Vexpad handset showing a red and white swirl candy screen"></div>
<div class="abs candy-photo" role="img" aria-label="Photo of a red and white peppermint candy"></div>
<div class="abs tagline">As Sweet As Candy</div>

<h2 class="abs section-label" style="left:134px;top:510px">Our Latest Apps</h2>
<div class="abs app-icon" role="img" aria-label="App icon showing a numbered scroll wheel"></div>
<h3 class="abs item-title" style="left:300px;top:566px">Niche Tabo App</h3>
<p class="abs item-text" style="left:302px;top:594px">Lorem ipsum dolor sit amet, consectetur<br>adipiscing elit. Quisque non ipsum enim.<br>Nunc rhoncus pretium fringilla. Nulla id ...</p>
<a class="abs more-link" style="left:302px;top:669px" href="#">Learn More</a>

<blockquote class="abs testimonial">“I had the chance to work with Plumwick on<br>my recent web application...Wow! I was<br>blown away by how they realized my vision.”</blockquote>
<div class="abs testimonial-author">Marla, USA</div>

<div class="abs divider"></div>

<h2 class="abs section-label" style="left:130px;top:730px">Latest Blog Post</h2>
<div class="abs post-date">10/26/2010</div>
<h3 class="abs item-title" style="left:299px;top:751px">Latest Blog Title</h3>
<p class="abs item-text" style="left:299px;top:776px">Lorem ipsum dolor sit amet, consectetur<br>adipiscing elit. Quisque non ipsum enim.</p>

<svg class="abs social-ribbon" width="117" height="74" viewBox="0 0 117 74" aria-hidden="true">
  <defs>
    <linearGradient id="ribbonFill" x1="0" y1="0" x2="0" y2="1">
      <stop offset="0" stop-color="#bcd3f3"/>
      <stop offset="1" stop-color="#8caee0"/>
    </linearGradient>
  </defs>
  <path d="M0 0 H117 V73 L58 56 L0 73 Z" fill="url(#ribbonFill)"/>
</svg>
<div class="abs social-name">chirpline</div>
<div class="abs social-follow">follow us</div>
<p class="abs update">* about 4 hours ago Plumwick<br>http://plumwick.com/blog/something-<br>interesting</p>

<footer class="abs site-footer"></footer>
<nav>
  <a class="abs footer-nav" style="left:131px" href="#">home</a>
  <a class="abs footer-nav" style="left:187px" href="#">apps</a>
  <a class="abs footer-nav" style="left:238px" href="#">support</a>
  <a class="abs footer-nav" style="left:308px" href="#">blog</a>
  <a class="abs footer-nav" style="left:356px" href="#">contact</a>
  <a class="abs footer-nav" style="left:423px" href="#">about</a>
</nav>

</body>
</html>
```